Managed IT services business card design

We haven't needed a business card since the founding of the business in 2005. All our clients have been coming through word of mouth. And lately more and more existing clients are requesting for our business cards to pass on to their contacts in recommending us.
So we needing a business card design. We use various innovative solutions and methodologies to provide IT services to small businesses in managing their IT systems. Our role is the same as an in-house, full-time IT Manager for our clients, but outsourced. So we take care of all our clients' IT needs, just as an IT Manager would be expected to perform.
We have a holding website, which we're happy to leave for now. If we can use the same logo would be great - www.tegvu.com.au
Preferred colours are shades of are white, grey and black.
We pride our business with the following traits: proactive, good service, prompt response, trustworthy.
Target Market(s)
Small businesses of any industry
Industry/Entity Type
Business

```html
<!DOCTYPE html>
<html lang="en">
<head>
<meta charset="utf-8">
<title>tegvu business card</title>
<link rel="stylesheet" href="https://fonts.googleapis.com/css2?family=Arimo:wght@400&display=swap">
<style>
  :root {
    --backdrop: #37332f;
    --card: #ffffff;
    --ink: #111111;
    --ink-soft: #333333;
    --rule: #222222;
  }
  html, body {
    margin: 0;
    padding: 0;
    width: 1200px;
    height: 1200px;
    overflow: hidden;
    background: var(--backdrop);
  }
  .canvas {
    position: relative;
    width: 1200px;
    height: 1200px;
    font-family: "Arimo", Arial, sans-serif;
  }
  .card {
    position: absolute;
    left: 153px;
    top: 342px;
    width: 893px;
    height: 516px;
    background: var(--card);
  }
  .brand {
    position: absolute;
    left: 0;
    width: 448px;
    text-align: center;
  }
  .brand-name {
    top: 212px;
    margin: 0;
    font-size: 40px;
    font-weight: 400;
    letter-spacing: 0.32em;
    text-indent: 0.32em;
    color: var(--ink);
  }
  .brand-tagline {
    top: 294px;
    margin: 0;
    font-size: 16.5px;
    color: var(--ink);
  }
  .divider {
    position: absolute;
    left: 448px;
    top: 64px;
    width: 1.5px;
    height: 386px;
    background: var(--rule);
  }
  .contact-list {
    list-style: none;
    margin: 0;
    padding: 0;
  }
  .contact-item {
    position: absolute;
    left: 496px;
    display: flex;
    align-items: center;
    height: 48px;
    margin-top: -24px;
  }
  .contact-item svg {
    width: 48px;
    height: 48px;
    flex: none;
  }
  .contact-text {
    margin-left: 32px;
    font-size: 21px;
    color: var(--ink-soft);
  }
  .contact-email { top: 163px; }
  .contact-phone { top: 261px; }
  .contact-address { top: 366px; }
</style>
</head>
<body>
<div class="canvas">
  <section class="card">
    <h1 class="brand brand-name">tegvu</h1>
    <p class="brand brand-tagline">managed i.t. services and consulting</p>
    <div class="divider"></div>
    <ul class="contact-list">
      <li class="contact-item contact-email">
        <svg viewBox="0 0 48 48" aria-hidden="true" fill="none" stroke="#222" stroke-width="1.5">
          <circle cx="24" cy="24" r="23"/>
          <rect x="13" y="16" width="22" height="16" rx="1"/>
          <polyline points="13,16 24,25 35,16"/>
        </svg>
        <span class="contact-text">mail@tegvu.com.au</span>
      </li>
      <li class="contact-item contact-phone">
        <svg viewBox="0 0 48 48" aria-hidden="true" fill="none" stroke="#222" stroke-width="1.5">
          <circle cx="24" cy="24" r="23"/>
          <rect x="17" y="12" width="14" height="24" rx="2"/>
          <rect x="19" y="15" width="10" height="16"/>
          <line x1="23" y1="33.5" x2="25" y2="33.5"/>
        </svg>
        <span class="contact-text">+61 400 555 218</span>
      </li>
      <li class="contact-item contact-address">
        <svg viewBox="0 0 48 48" aria-hidden="true" fill="none" stroke="#222" stroke-width="1.5">
          <circle cx="24" cy="24" r="23"/>
          <polyline points="11,24 24,13 37,24"/>
          <polyline points="15,21 15,33 33,33 33,21"/>
        </svg>
        <span class="contact-text">little ferncourt, melbourne</span>
      </li>
    </ul>
  </section>
</div>
</body>
</html>
```